Healthcare/Medical Consultant Company

KTL is a Healthcare Conultant Company. We help doctors manage the business side of their medical practice.
We already have a very basic world press design. We want an upgraded design that conveys partnership, healthcare expertise and healthcare innovation to our client. It needs to have a sleek, clean, modern and inclusive look. Pictures need need to convey diversity (including pictures of people of all races and shows both men and women working together in a healthcare environment to make it better). The Pictures on the home page should particularly illustrate diversity and Healthcare expertise. The company logo is blue and white but the site doesn’t have to follow the exact same theme but the logo needs to blend well with the chosen theme. The logo should ideally be in the header of the website. We would also like the following included in our website:

1. Pages should include: a home page, About Us page, Services page, Get a quote page, Contact Us page, Staff page(where we can add pictures and bio for staff).

2. The Drop down menu for services should have hyperlinks ( for each service)Leading to a page that provides detailed info about that specific service. Our services include: Revenue Cycle Management, Regulatory Compliance, Human Resources Management, & practice Management.

3. Links to social media should in the header or footer of each page.

4. Contact info should be in the footer of each page.

5. Clients should be an email to us from the contact page.

Target Market(s)

Physician Medical Practices

Industry/Entity Type

Medical

Coding

Coded - Design and coding required

Font styles to use
Sans Serif

Colors

Designer to choose colors to be used in the design.

Requirements
Must have
• See project description
Nice to have
• See project description

```html
<!DOCTYPE html>
<html lang="en">
<head>
<meta charset="utf-8">
<title>KTL Health Partners — Advancing Healthcare</title>
<link rel="stylesheet" href="https://fonts.googleapis.com/css2?family=Lora:wght@400;500&family=Open+Sans:wght@400;600&display=swap">
<style>
:root{
  --brand:#0d3c8f;
  --brand-bright:#2a74c4;
  --ink:#1b1b1b;
  --body:#555a60;
  --muted:#8a8f95;
  --line:#9aa0a6;
  --panel:#efefef;
  --footer:#2b2b2b;
  --footer-bar:#1f1f1f;
  --footer-text:#b9b9b9;
  --white:#ffffff;
}
*{margin:0;padding:0;box-sizing:border-box}
html,body{width:1200px;height:2419px;overflow:hidden;background:var(--white)}
body{position:relative;font-family:"Open Sans",Arial,sans-serif;color:var(--body)}

/* header */
.site-header{position:absolute;left:0;top:0;width:1200px;height:122px;background:var(--white)}
.brand{position:absolute;left:132px;top:30px;display:flex;align-items:center;gap:12px;font-family:"Lora",Georgia,serif;font-size:30px;color:var(--brand);font-weight:500}
.brand-mark{width:18px;height:18px;background:var(--brand);border-radius:50%}
.quote-btn{position:absolute;left:932px;top:24px;width:135px;height:38px;background:var(--brand);color:var(--white);font-family:"Lora",Georgia,serif;font-size:16px;display:flex;align-items:center;justify-content:center;letter-spacing:.3px}
.main-nav{position:absolute;right:133px;top:80px;display:flex;gap:40px;font-family:"Lora",Georgia,serif;font-size:16px;color:#5c5f63;letter-spacing:.4px}
.main-nav .active{color:var(--brand-bright)}

/* hero */
.hero{position:absolute;left:0;top:122px;width:1200px;height:493px;background:linear-gradient(100deg,#3d5a4c 0%,#8f8f86 22%,#c7c3bd 45%,#6f7f94 62%,#b9b6b1 80%,#3a3f46 100%)}
.hero-arrow{position:absolute;top:230px;width:22px;height:34px}
.hero-caption{position:absolute;left:132px;top:360px;width:415px;height:92px;background:rgba(255,255,255,.78);padding:12px 16px;font-family:"Lora",Georgia,serif;color:#333}
.hero-caption .line1{font-size:25px;line-height:32px}
.hero-caption .line2{font-size:27px;line-height:34px;font-weight:500;letter-spacing:.5px}

/* welcome */
.welcome-photo{position:absolute;left:132px;top:695px;width:307px;height:283px;background:linear-gradient(135deg,#d9dde2 0%,#a9b3c0 50%,#2c3f6b 100%)}
.welcome-title{position:absolute;left:463px;top:688px;font-family:"Lora",Georgia,serif;font-size:33px;color:var(--brand);font-weight:400}
.welcome-text{position:absolute;left:463px;top:740px;width:606px;font-size:11.4px;line-height:22.4px;color:var(--body)}
.btn-outline{position:absolute;border:1px solid var(--line);color:#555;display:flex;align-items:center;justify-content:center;background:var(--white)}
.welcome-more{left:463px;top:935px;width:115px;height:43px;font-family:"Lora",Georgia,serif;font-size:15px}

/* services */
.services{position:absolute;left:0;top:1058px;width:1200px;height:550px;background:var(--panel)}
.section-title{position:absolute;left:0;width:1200px;text-align:center;font-family:"Lora",Georgia,serif;font-size:33px;color:var(--brand);font-weight:400}
.service-card{position:absolute;width:454px;height:154px;background:var(--brand);color:var(--white)}
.service-card svg{position:absolute;left:22px;top:20px}
.service-card h3{position:absolute;left:124px;top:14px;font-family:"Lora",Georgia,serif;font-weight:400;font-size:17px;white-space:nowrap}
.service-card p{position:absolute;left:124px;top:46px;width:314px;font-size:9px;line-height:16px;letter-spacing:-.05px;color:#e6ecf7}
.service-card .card-btn{position:absolute;left:124px;top:104px;width:84px;height:30px;border:1px solid var(--white);font-size:11.5px;display:flex;align-items:center;justify-content:center}

/* blog */
.blog-photo{position:absolute;top:1744px;height:189px}
.blog-title{position:absolute;top:1943px;width:298px;font-size:16px;line-height:22px;color:var(--ink);font-weight:400}
.blog-text{position:absolute;top:1993px;width:298px;font-size:10.6px;line-height:17.5px;color:var(--body)}
.blog-more{top:2061px;width:84px;height:31px;font-size:11.5px}

/* footer */
.site-footer{position:absolute;left:0;top:2172px;width:1200px;height:196px;background:var(--footer);color:var(--footer-text)}
.footer-heading{position:absolute;top:42px;font-family:"Lora",Georgia,serif;font-size:19px;color:#e8e8e8;font-weight:400}
.contact-row{position:absolute;left:132px;display:flex;align-items:center;gap:14px;font-size:11.5px}
.footer-links{position:absolute;font-size:11.5px;line-height:25.5px}
.social{position:absolute;top:83px;width:36px;height:36px;border-radius:50%;background:#5d5d5d}
.footer-bar{position:absolute;left:0;top:2368px;width:1200px;height:51px;background:var(--footer-bar);color:#9a9a9a;font-size:11.5px;display:flex;align-items:center;justify-content:center}
</style>
</head>
<body>

<header class="site-header">
  <div class="brand"><span class="brand-mark"></span>KTL Health Partners</div>
  <div class="quote-btn">GET A QUOTE</div>
  <nav class="main-nav">
    <span class="active">HOME</span><span>ABOUT US</span><span>SERVICES</span><span>STAFF</span><span>CONTACT US</span>
  </nav>
</header>

<section class="hero" role="img" aria-label="Diverse team of doctors and consultants reviewing documents together around a table">
  <svg class="hero-arrow" style="left:46px" viewBox="0 0 22 34"><path d="M18 3 L5 17 L18 31" fill="none" stroke="#fff" stroke-width="5"/></svg>
  <svg class="hero-arrow" style="left:1132px" viewBox="0 0 22 34"><path d="M4 3 L17 17 L4 31" fill="none" stroke="#fff" stroke-width="5"/></svg>
  <div class="hero-caption">
    <div class="line1">KTL Health Partners</div>
    <div class="line2">“ADVANCING HEALTHCARE”</div>
  </div>
</section>

<div class="welcome-photo" role="img" aria-label="Nurse and doctor discussing a chart in front of a whiteboard"></div>
<h1 class="welcome-title">Welcome to KTL Health Partners</h1>
<p class="welcome-text">KTL Health Partners (KTL) is a healthcare consulting firm skilled at helping physician practices advance their strategic vision in an ever-evolving healthcare system. KTL Health Partners specializes in revenue cycle optimization, practice management improvement and developing new physician practices. Our technical skills allow us to dig deep into your revenue cycle while our strategic approach ensures we're keeping our eyes on the entire financial picture. By implementing a comprehensive approach to optimization and working closely with your people, processes, and technology, we develop a complete picture of your organization's performance. More importantly, we're able to design strategies and solutions that improve this performance while also preserving your organization's mission, vision, and strategic initiatives.</p>
<div class="btn-outline welcome-more">Read More</div>

<section class="services">
  <h2 class="section-title" style="top:70px">Services</h2>

  <div class="service-card" style="left:132px;top:130px">
    <svg width="80" height="80" viewBox="0 0 80 80" fill="none" stroke="#fff" stroke-width="3.5" stroke-linecap="round">
      <path d="M20 48 A22 22 0 0 1 52 18"/><path d="M44 12 L54 18 L46 27"/>
      <path d="M60 32 A22 22 0 0 1 28 62"/><path d="M36 68 L26 62 L34 53"/>
    </svg>
    <h3>Revenue Cycle Management</h3>
    <p>In today's increasingly complex health care environment it's important now more than ever that medical practices closely manage their revenue cycle.</p>
    <div class="card-btn">Read More</div>
  </div>

  <div class="service-card" style="left:613px;top:130px">
    <svg width="80" height="80" viewBox="0 0 80 80" fill="none" stroke="#fff" stroke-width="2.5">
      <rect x="3" y="2" width="74" height="76"/>
      <path d="M30 24 H66 M30 40 H66 M30 56 H66"/>
      <g fill="#fff" stroke="none"><circle cx="18" cy="24" r="4"/><circle cx="18" cy="40" r="4"/><circle cx="18" cy="56" r="4"/></g>
    </svg>
    <h3>Regulatory &amp; Compliance Management</h3>
    <p>In a heavily regulated healthcare environment medical practices need to be acutely aware of regulations as they present huge liabilities. It is extremely important to ensure compliance with regulations</p>
    <div class="card-btn">Read More</div>
  </div>

  <div class="service-card" style="left:132px;top:316px">
    <svg width="80" height="90" viewBox="0 0 80 90" fill="none" stroke="#fff" stroke-width="3" stroke-linecap="round">
      <path d="M10 6 V30 A14 14 0 0 0 38 30 V6"/>
      <path d="M24 44 V60 A14 14 0 0 0 52 60 V52"/>
      <circle cx="56" cy="44" r="8"/>
    </svg>
    <h3>Practice Management</h3>
    <p>Practice Management is challenging and it requires the right balance of skill, knowledge, experience and management expertise. KTL Offers assessment and optimization</p>
    <div class="card-btn">Read More</div>
  </div>

  <div class="service-card" style="left:613px;top:316px">
    <svg width="84" height="80" viewBox="0 0 84 80" fill="none" stroke="#fff" stroke-width="2.5">
      <circle cx="22" cy="24" r="9"/><circle cx="62" cy="24" r="9"/><circle cx="42" cy="20" r="11"/>
      <path d="M6 72 V52 A14 14 0 0 1 20 40 H24"/><path d="M78 72 V52 A14 14 0 0 0 64 40 H60"/>
      <path d="M22 74 V52 A14 14 0 0 1 36 38 H48 A14 14 0 0 1 62 52 V74 Z"/>
    </svg>
    <h3>Human Resources Management</h3>
    <p>Not having a full service Human Resources Department can increase liability and be costly to your medical practice. Do you need Human Resources Management</p>
    <div class="card-btn">Read More</div>
  </div>
</section>

<h2 class="section-title" style="top:1676px">Blog</h2>

<div class="blog-photo" style="left:132px;width:298px;background:linear-gradient(135deg,#eceae6,#b8b4ad 60%,#6d7480)" role="img" aria-label="Two colleagues meeting at a desk with a laptop"></div>
<div class="blog-photo" style="left:452px;width:297px;background:linear-gradient(135deg,#e6e9ec,#a8aeb6 55%,#7d3a4a)" role="img" aria-label="Two professionals in discussion at a table in a bright office"></div>
<div class="blog-photo" style="left:771px;width:296px;background:linear-gradient(135deg,#f1f1f1,#c3c6ca 50%,#3c4a62)" role="img" aria-label="Doctor talking with business colleagues in a clinic"></div>

<h3 class="blog-title" style="left:132px">Pellentesque convallis molestie enim sit amet efficitur</h3>
<h3 class="blog-title" style="left:452px">Cras augue magna, placerat eget nulla non, congue suscipit neque</h3>
<h3 class="blog-title" style="left:771px">Vestibulum ante primis in faucibus orci luctus et ultrices</h3>

<p class="blog-text" style="left:132px">Fusce vitae lectus sit amet mi pulvinar maximus. Aenean placerat, nibh vel accumsan aliquet, magna nibh accumsan nibh, ac tempus nunc ipsum ac tellus.</p>
<p class="blog-text" style="left:452px">Fusce vitae lectus sit amet mi pulvinar maximus. Aenean placerat, nibh vel accumsan aliquet, magna nibh accumsan nibh, ac tempus nunc ipsum ac tellus.</p>
<p class="blog-text" style="left:771px">Fusce vitae lectus sit amet mi pulvinar maximus. Aenean placerat, nibh vel accumsan aliquet, magna nibh accumsan nibh, ac tempus nunc ipsum ac tellus.</p>

<div class="btn-outline blog-more" style="left:132px">Read More</div>
<div class="btn-outline blog-more" style="left:452px">Read More</div>
<div class="btn-outline blog-more" style="left:771px">Read More</div>

<footer class="site-footer">
  <h4 class="footer-heading" style="left:132px">Contact info</h4>
  <div class="contact-row" style="top:84px">
    <svg width="10" height="12" viewBox="0 0 10 12"><path d="M5 0 A4.5 4.5 0 0 1 9.5 4.5 C9.5 8 5 12 5 12 S0.5 8 0.5 4.5 A4.5 4.5 0 0 1 5 0 Z" fill="#b9b9b9"/><circle cx="5" cy="4.5" r="1.7" fill="#2b2b2b"/></svg>
    <span>18 Harbor Lane Suite 300 Fairview, NY 10990</span>
  </div>
  <div class="contact-row" style="top:110px">
    <svg width="10" height="12" viewBox="0 0 10 12"><path d="M2 0 L4 3 L3 5 C4 7 5 8 7 9 L9 8 L10 10 L8 12 C4 11 0 6 0 2 Z" fill="#b9b9b9"/></svg>
    <span>Voice: (555) 014-2290</span>
  </div>
  <div class="contact-row" style="top:136px">
    <svg width="12" height="10" viewBox="0 0 12 10"><rect width="12" height="10" fill="#b9b9b9"/><path d="M0 0 L6 5 L12 0" fill="none" stroke="#2b2b2b" stroke-width="1.2"/></svg>
    <span>Email: info@ktlhealthpartners.example</span>
  </div>

  <h4 class="footer-heading" style="left:600px">Links</h4>
  <div class="footer-links" style="left:600px;top:78px">Home<br>About Us<br>Services</div>
  <div class="footer-links" style="left:680px;top:78px">Staff<br>Contact Us</div>

  <h4 class="footer-heading" style="left:935px">Follow us on</h4>
  <span class="social" style="left:935px" aria-label="Social profile one"></span>
  <span class="social" style="left:983px" aria-label="Social profile two"></span>
  <span class="social" style="left:1031px" aria-label="Social profile three"></span>
</footer>
<div class="footer-bar">Copyright © 2018 KTL Health Partners. All rights reserved.</div>

</body>
</html>
```